Yard Signs - Fiber Optic Customer

I need an awesome design for a yard sign for our new customers.  We are installing a fiber optic network and are going to give new customers the option to put a yard sign up in exchange for a free month of service.  I want to use printholm-example.com.  A blank template is available there for the large (27x18) yard signs.
Requirements:
-our website is (needs to be on sign):  www.brindlelinknet.example
-our phone:  402-555-0148
-our logo
-a graphic that conveys 'connected'
I want it to say something to the effect.. I'm connected to Brindle Fiber.  The fastest high-speed internet available.  Crystal clear telephone.  I don't necessarily need that specific wording, something along those lines.
Contact me with questions:  owen@brindlelinknet.example

Industry/Entity Type
Internet

```html
<!DOCTYPE html>
<html lang="en">
<head>
<meta charset="UTF-8">
<title>Brindle Fiber Yard Sign</title>
<link rel="stylesheet" href="https://fonts.googleapis.com/css2?family=Source+Sans+3:ital,wght@0,400;0,700;1,400;1,700&display=swap">
<style>
  :root {
    --page-bg: #eceef0;
    --sign-white: #ffffff;
    --brand-teal: #1b7d9f;
    --deep-navy: #0d2a4a;
    --mid-blue: #1f5d93;
    --glow-blue: #5fa6dc;
    --text-white: #ffffff;
  }
  * { margin: 0; padding: 0; box-sizing: border-box; }
  html, body {
    width: 1200px;
    height: 900px;
    overflow: hidden;
    background: var(--page-bg);
    font-family: "Source Sans 3", "Myriad Pro", Arial, sans-serif;
  }
  .yard-sign {
    position: absolute;
    left: 30px;
    top: 70px;
    width: 1140px;
    height: 760px;
    background: var(--sign-white);
    overflow: hidden;
    box-shadow: 0 2px 10px rgba(0,0,0,0.15);
  }
  .brand-band {
    position: absolute;
    top: 0; left: 0;
    width: 100%;
    height: 195px;
    display: flex;
    align-items: center;
    justify-content: center;
  }
  .brand-name {
    font-weight: 700;
    font-size: 124px;
    letter-spacing: 2px;
    color: var(--brand-teal);
    line-height: 1;
  }
  .fiber-photo {
    position: absolute;
    top: 175px; left: 0;
    width: 100%;
    height: 585px;
    background:
      radial-gradient(ellipse at 70% 35%, rgba(150,205,245,0.55) 0%, rgba(95,166,220,0.25) 30%, transparent 60%),
      radial-gradient(ellipse at 15% 75%, rgba(95,166,220,0.35) 0%, transparent 45%),
      linear-gradient(to bottom, var(--sign-white) 0%, #b9cde0 8%, var(--mid-blue) 22%, var(--deep-navy) 62%, var(--mid-blue) 100%);
  }
  .message {
    position: absolute;
    left: 0;
    width: 100%;
    text-align: center;
    color: var(--text-white);
    font-style: italic;
    font-size: 38px;
    line-height: 60px;
    top: 295px;
    text-shadow: 0 1px 3px rgba(0,0,0,0.35);
  }
  .phone {
    position: absolute;
    left: 0;
    width: 100%;
    top: 543px;
    display: flex;
    justify-content: center;
    align-items: center;
    gap: 8px;
    color: var(--text-white);
    font-weight: 700;
    font-style: italic;
    font-size: 76px;
    line-height: 1;
    text-shadow: 0 1px 3px rgba(0,0,0,0.35);
  }
  .phone-icon { width: 48px; height: 48px; }
  .website {
    position: absolute;
    left: 0;
    width: 100%;
    top: 657px;
    text-align: center;
    color: var(--text-white);
    font-size: 44px;
    letter-spacing: 5px;
    line-height: 1;
  }
</style>
</head>
<body>
  <div class="yard-sign">
    <div class="fiber-photo" role="img" aria-label="Photo of glowing blue fiber optic strands and network cables"></div>
    <div class="brand-band">
      <span class="brand-name">BRINDLE</span>
    </div>
    <p class="message">
      I'm connected to Brindle FIBER!!<br>
      The fastest high-speed internet available..<br>
      Crystal clear telephone.
    </p>
    <div class="phone">
      <svg class="phone-icon" viewBox="0 0 24 24" aria-hidden="true">
        <path fill="#ffffff" d="M6.6 10.8c1.4 2.8 3.8 5.1 6.6 6.6l2.2-2.2c.3-.3.7-.4 1-.2 1.1.4 2.3.6 3.6.6.6 0 1 .4 1 1V20c0 .6-.4 1-1 1C10.6 21 3 13.4 3 4c0-.6.4-1 1-1h3.5c.6 0 1 .4 1 1 0 1.3.2 2.5.6 3.6.1.3 0 .7-.2 1z"/>
      </svg>
      <span>402-555-0148</span>
    </div>
    <p class="website">www.brindlelinknet.example</p>
  </div>
</body>
</html>
```